Letterhead & Business Card Design Project

Use existing logo to create a new letterhead and business card design. Looking for something clean modern using color options of black, white and gray. The green from the logo may be used lightly as an accent color.

Target Market(s)

Professional business people

Industry/Entity Type

Business

Requirements
Must have
• Business card with front and back design using existing logo.
Nice to have
• Professional presentation
Clean look
Should not have
• No oil rigs, pumpjacks or clip art.

```html
<!DOCTYPE html>
<html lang="en">
<head>
<meta charset="utf-8">
<title>Halvorsen Exploration – Letterhead</title>
<link rel="stylesheet" href="https://fonts.googleapis.com/css2?family=Open+Sans:wght@400&display=swap">
<style>
  :root {
    --ink: #111111;
    --paper: #ffffff;
    --footer-band: #3a3a3a;
    --footer-text: #c9c9c9;
    --accent-green: #3cc43c;
  }
  html, body {
    margin: 0;
    padding: 0;
    overflow: hidden;
    background: var(--paper);
  }
  .letterhead {
    position: relative;
    width: 847px;
    height: 1200px;
    background: var(--paper);
    overflow: hidden;
    font-family: "Open Sans", Arial, sans-serif;
  }
  .corner-block {
    position: absolute;
    left: 0;
    top: 0;
    width: 49px;
    height: 122px;
    background: var(--ink);
  }
  .corner-accent {
    position: absolute;
    left: 49px;
    top: 0;
    width: 4px;
    height: 122px;
    background: var(--accent-green);
  }
  .company-name {
    position: absolute;
    left: 80px;
    top: 38px;
    margin: 0;
    font-size: 27px;
    font-weight: 400;
    letter-spacing: 4px;
    text-transform: uppercase;
    color: var(--ink);
    line-height: 1;
  }
  .footer-band {
    position: absolute;
    left: 0;
    bottom: 0;
    width: 832px;
    height: 31px;
    background: var(--footer-band);
    color: var(--footer-text);
    font-size: 14px;
    line-height: 31px;
    text-align: center;
    white-space: nowrap;
  }
  .footer-accent {
    position: absolute;
    right: 0;
    bottom: 0;
    width: 13px;
    height: 31px;
    background: var(--accent-green);
  }
</style>
</head>
<body>
  <main class="letterhead">
    <div class="corner-block"></div>
    <div class="corner-accent"></div>
    <h1 class="company-name">Halvorsen Exploration</h1>

    <footer class="footer-band">
      Halvorsen Exploration, 4420 North Cedar Ave, Suite 210, Tulsa, OK 74105 Phone 918.555.0142 Fax 918.555.0143
    </footer>
    <div class="footer-accent"></div>
  </main>
</body>
</html>
```